New company business cards with new company logo

We need a new business card designed as we have a new company logo and are going for a more 'flat design' look. Our company name is Veridanto and we are a global data focused Clinical Research Organisation. We'd ideally like one side with room for the individuals contact details, our full logo and our services - and one side which is quite plain, for example perhaps using the green triangular image attached with just the white 'V' in the center (also attached).

Industry/Entity Type

Business

Requirements
Must have
• Our main colour: #42b5a9
Please make text dark grey: #373737

```html
<!DOCTYPE html>
<html lang="en">
<head>
<meta charset="utf-8">
<title>Veridanto Business Card</title>
<link href="https://fonts.googleapis.com/css2?family=Open+Sans:wght@400;600;700&display=swap" rel="stylesheet">
<style>
  :root {
    --brand: #42b5a9;
    --brand-deep: #2e9186;
    --brand-soft: #8fcbc3;
    --text: #373737;
    --paper: #ffffff;
    --backdrop: #ececec;
  }
  * { box-sizing: border-box; margin: 0; padding: 0; }
  html, body {
    width: 1200px; height: 726px; overflow: hidden;
    background: var(--backdrop);
    font-family: "Open Sans", Arial, sans-serif;
    color: var(--text);
  }
  .canvas {
    position: relative; width: 1200px; height: 726px;
  }
  .card {
    position: absolute; top: 214px;
    width: 520px; height: 297px;
    overflow: hidden;
    box-shadow: 0 4px 14px rgba(0,0,0,0.12);
  }
  /* Plain side */
  .card--back { left: 50px; }
  .back-field {
    position: absolute; inset: 0;
    background: linear-gradient(135deg, var(--brand-soft) 0%, #7fc2b9 45%, var(--brand-soft) 100%);
  }
  .back-emblem {
    position: absolute; left: 50%; top: 50%;
    width: 132px; height: 132px; margin: -66px 0 0 -66px;
    border-radius: 50%; background: var(--paper);
    display: flex; align-items: center; justify-content: center;
    font-weight: 600; font-size: 20px; color: var(--brand);
  }
  /* Contact side */
  .card--front { left: 630px; background: var(--paper); }
  .front-disc {
    position: absolute; left: -250px; top: 60px;
    width: 440px; height: 440px; border-radius: 50%;
    background: var(--brand-deep);
  }
  .brand-lockup {
    position: absolute; right: 26px; top: 34px;
    display: flex; align-items: center; gap: 10px;
  }
  .brand-dot {
    width: 50px; height: 50px; border-radius: 50%; background: var(--brand-deep);
  }
  .brand-name {
    font-size: 30px; font-weight: 400; line-height: 1; color: var(--text);
    letter-spacing: -0.5px;
  }
  .brand-tagline {
    margin-top: 4px; padding-top: 2px;
    border-top: 1px solid var(--text);
    font-size: 9.5px; color: var(--brand-deep); letter-spacing: 0.6px;
  }
  .person {
    position: absolute; right: 26px; top: 104px; text-align: right;
  }
  .person-name { font-size: 15px; font-weight: 700; color: var(--brand-deep); }
  .person-role { font-size: 10px; color: var(--text); }
  .contact-list {
    position: absolute; right: 20px; top: 168px;
    list-style: none; text-align: right;
    font-size: 12px; line-height: 19px;
  }
  .contact-list li { display: flex; justify-content: flex-end; align-items: center; gap: 6px; }
  .contact-icon { width: 11px; height: 11px; fill: var(--brand-deep); }
</style>
</head>
<body>
<main class="canvas">
  <section class="card card--back">
    <div class="back-field" role="img" aria-label="Faceted green triangular background pattern"></div>
    <div class="back-emblem">Veridanto</div>
  </section>

  <section class="card card--front">
    <div class="front-disc"></div>

    <div class="brand-lockup">
      <span class="brand-dot"></span>
      <div>
        <div class="brand-name">Veridanto</div>
        <div class="brand-tagline">A Passion For Excellence</div>
      </div>
    </div>

    <div class="person">
      <div class="person-name">Your Long Name</div>
      <div class="person-role">Managing Director</div>
    </div>

    <ul class="contact-list">
      <li>Your Commercial or office address
        <svg class="contact-icon" viewBox="0 0 12 12"><path d="M6 0a4 4 0 0 0-4 4c0 3 4 8 4 8s4-5 4-8a4 4 0 0 0-4-4zm0 5.5A1.5 1.5 0 1 1 6 2.5a1.5 1.5 0 0 1 0 3z"/></svg>
      </li>
      <li>00.00.00.0000
        <svg class="contact-icon" viewBox="0 0 12 12"><path d="M1 3c0-1 1-2 2-2h6c1 0 2 1 2 2v1H8V3H4v1H1zM2 5h8l1 6H1z"/></svg>
        00.00.00.0000
        <svg class="contact-icon" viewBox="0 0 12 12"><path d="M2 1h6v3h2v7H2zM3 2v2h4V2zM3 6h2v1H3zm3 0h2v1H6zM3 8h2v1H3zm3 0h2v1H6z"/></svg>
      </li>
      <li>yourname@veridanto.com
        <svg class="contact-icon" viewBox="0 0 12 12"><path d="M0 2h12v1L6 7 0 3zM0 4.2l6 4 6-4V10H0z"/></svg>
      </li>
      <li>www.veridanto.com
        <svg class="contact-icon" viewBox="0 0 12 12"><path d="M6 0a6 6 0 1 0 0 12A6 6 0 0 0 6 0zm0 1c.8 0 1.6 1.8 1.8 4.5H4.2C4.4 2.8 5.2 1 6 1zM1 6.5h2.2c.1 1.6.4 3 .9 3.9A5 5 0 0 1 1 6.5zm0-1a5 5 0 0 1 3.1-3.9c-.5.9-.8 2.3-.9 3.9zm5 5.5c-.8 0-1.6-1.8-1.8-4.5h3.6C7.6 9.2 6.8 11 6 11zm1.9-.6c.5-.9.8-2.3.9-3.9H11a5 5 0 0 1-3.1 3.9zM8.8 5.5c-.1-1.6-.4-3-.9-3.9A5 5 0 0 1 11 5.5z"/></svg>
      </li>
    </ul>
  </section>
</main>
</body>
</html>
```